Kettle Ledger Business Card design

We need a stand out business card design for Accounting practice based in Australia specialising in pubs, clubs and hotels. We help venues maximise margins, create time and manage cashflow. One club we have been working with for the last 6 months has increased revenue by 3% and margin by 5% in this time frame. We have a back office outsourced system that costs less than having a full time employee and also allows the venues the added benefit of:<br/>-using the office space to become a revenue generating opportunity. <br/>-a complete system to enhance governance, accountability and efficiency within their operation<br/>-52 weeks cover so no hassle to cover annual/sick .. leave<br/><br/>We would like to see designs that use the colours of our logo (green & blue).
Target Market(s)
Australian Pubs, Clubs & Hotels abookkeeping, accounting and tax services
Industry/Entity Type
Accountant
Contact Information for Business Card
Miriam Oakley CPA
Principal
Accountant Tax Agent
Miriam@KettleLedger-example.com.au
0418693142
www.kettleledger-example.com.au
Accounting / Payroll / Tax / SMSF / Technology
Colors
Designer to choose colors to be used in the design.
Look and feel
Each slider illustrates characteristics of the customer's brand and the style your logo design should communicate.

```html
<!DOCTYPE html>
<html lang="en">
<head>
<meta charset="utf-8">
<title>Kettle Ledger Business Card</title>
<link rel="stylesheet" href="https://fonts.googleapis.com/css2?family=Arimo:wght@400;700&family=Noto+Serif:wght@400&display=swap">
<style>
  :root {
    --backdrop: #d6d6d6;
    --card-dark: #5a5a5c;
    --card-light: #f7f7f5;
    --brand-blue: #1f3f95;
    --brand-green: #2e8b3e;
    --ink: #1d1d1d;
    --white: #ffffff;
  }
  * { box-sizing: border-box; margin: 0; padding: 0; }
  html, body { width: 1200px; height: 800px; overflow: hidden; }
  body {
    background: var(--backdrop);
    font-family: "Arimo", Arial, sans-serif;
    position: relative;
  }
  .card {
    position: absolute;
    top: 250px;
    width: 520px;
    height: 300px;
    border-radius: 20px;
    box-shadow: 0 6px 18px rgba(0,0,0,0.18);
  }
  /* Front */
  .card-front {
    left: 50px;
    background: var(--card-dark);
    color: var(--white);
  }
  .front-brand {
    position: absolute;
    left: 0; right: 0; top: 96px;
    display: flex;
    align-items: center;
    justify-content: center;
    gap: 16px;
  }
  .brand-dot {
    width: 40px; height: 40px;
    border-radius: 50%;
    background: var(--white);
  }
  .front-brand .brand-name {
    font-weight: 700;
    font-size: 46px;
    letter-spacing: -0.5px;
  }
  .services {
    position: absolute;
    left: 0; right: 0; bottom: 40px;
    text-align: center;
    font-family: "Noto Serif", "Times New Roman", serif;
    font-size: 17px;
    letter-spacing: 0.5px;
  }
  /* Back */
  .card-back {
    left: 630px;
    background: var(--card-light);
  }
  .back-brand {
    position: absolute;
    left: 34px; top: 40px;
    display: flex;
    align-items: center;
    gap: 10px;
    color: var(--brand-blue);
  }
  .back-brand .brand-dot {
    width: 28px; height: 28px;
    background: var(--brand-green);
  }
  .back-brand .brand-name {
    font-weight: 700;
    font-size: 24px;
  }
  .divider {
    position: absolute;
    left: 34px; right: 34px; top: 100px;
    height: 2px;
    background: var(--brand-blue);
    opacity: 0.8;
  }
  .person {
    position: absolute;
    left: 34px; top: 118px;
  }
  .person-name {
    color: var(--brand-blue);
    font-weight: 700;
    font-size: 21px;
    letter-spacing: 0.3px;
  }
  .person-role {
    color: var(--brand-green);
    font-weight: 700;
    font-size: 15px;
    margin-top: 4px;
  }
  .contacts {
    position: absolute;
    left: 34px; top: 186px;
    list-style: none;
  }
  .contacts li {
    display: flex;
    align-items: center;
    gap: 10px;
    color: var(--ink);
    font-size: 15px;
    height: 26px;
  }
  .contact-icon {
    width: 18px; height: 18px;
    flex: none;
  }
</style>
</head>
<body>
  <section class="card card-front" aria-label="Business card front">
    <div class="front-brand">
      <span class="brand-dot"></span>
      <span class="brand-name">Kettle Ledger</span>
    </div>
    <p class="services">Accounting / Payroll / Tax / SMSF / Technology</p>
  </section>

  <section class="card card-back" aria-label="Business card back">
    <div class="back-brand">
      <span class="brand-dot"></span>
      <span class="brand-name">Kettle Ledger</span>
    </div>
    <div class="divider"></div>
    <div class="person">
      <p class="person-name">Miriam Oakley CPA</p>
      <p class="person-role">Principal</p>
    </div>
    <ul class="contacts">
      <li>
        <svg class="contact-icon" viewBox="0 0 20 20" aria-hidden="true">
          <circle cx="10" cy="10" r="9" fill="none" stroke="#2e8b3e" stroke-width="1.5"/>
          <path d="M7 5.5 L8.5 5.5 L9.3 8 L8.2 9 Q9 11 11 11.8 L12 10.7 L14.5 11.5 L14.5 13 Q14 14.5 12 14.2 Q7 13 5.8 8 Q5.5 6 7 5.5 Z" fill="#2e8b3e"/>
        </svg>
        0418693142
      </li>
      <li>
        <svg class="contact-icon" viewBox="0 0 20 20" aria-hidden="true">
          <circle cx="10" cy="10" r="9" fill="none" stroke="#2e8b3e" stroke-width="1.5"/>
          <rect x="5" y="6.5" width="10" height="7" fill="none" stroke="#2e8b3e" stroke-width="1.3"/>
          <path d="M5 6.5 L10 10.5 L15 6.5" fill="none" stroke="#2e8b3e" stroke-width="1.3"/>
        </svg>
        Miriam@KettleLedger-example.com.au
      </li>
      <li>
        <svg class="contact-icon" viewBox="0 0 20 20" aria-hidden="true">
          <circle cx="10" cy="10" r="9" fill="none" stroke="#2e8b3e" stroke-width="1.5"/>
          <circle cx="10" cy="10" r="5" fill="none" stroke="#2e8b3e" stroke-width="1.2"/>
          <ellipse cx="10" cy="10" rx="2.2" ry="5" fill="none" stroke="#2e8b3e" stroke-width="1.2"/>
          <path d="M5 10 H15" stroke="#2e8b3e" stroke-width="1.2"/>
        </svg>
        www.kettleledger-example.com.au
      </li>
    </ul>
  </section>
</body>
</html>
```